Pinecrest Treatment Brochure for a drug and alcohol addiction treatment center.

***Update #2***
For graphic highlights no intrusion into text and no fade into adjoining areas.Use modern clean white layout with grey and light orange color scheme. Use attached yoga photo and other photos. For cover try moving number and logo around, and also try with cover photo not full size. Also use larger text with bullet points in a couple spots. Also try with new attached cover photos.
***Update*** I have attached some new photos to clarify the design wanted. My client likes the size (but not design) of the brochure in the newly included photos. Note the measurements - when closed it is 6" wide x 7" tall. When fully open it is 18" long, 7" wide, with 2 folds. I apologize if my terminology below was confusing. Please confirm that your design reflects the desired layout, and please modify your design if it does not. Thanks!
Want a trifold brochure 6" wide x 7" height. Design is for a drug and alcohol addiction treatment center. We want clean, soft, contemporary with highlight colors orange and grey, with contemporary font. Maybe some soft curves on design - see this A4 design we like but not the colors:
http://stockmosaic.example/item/corporate-folded-leaflet-ripple/7391052?s_phrase=trifold%20business%20brochure&s_rank=54
See company web site for style cues and some content you can use:
http://pinecrestcarehub.example/
You can use the attached photos and logo in the design. Try sun in hand photo on cover, or man on beach. Please do not use the words "The Pinecrest Treatment Center" in verbiage or titles, for business reasons we want to use "Pinecrest Treatment Center" with no "The" instead.
Please note that the logo has been updated. The new logo is attached below. Use pinecrest rev2.png for logo.
Addiction treatment industry professionals; family and decision makers of addict; addict themselves.
Health And Wellness

```html
<!DOCTYPE html>
<html lang="en">
<head>
<meta charset="utf-8">
<title>Pinecrest Treatment Center – Brochure Spread</title>
<link href="https://fonts.googleapis.com/css2?family=Questrial&family=Mulish:wght@600;700&family=Open+Sans:wght@400;700&display=swap" rel="stylesheet">
<style>
  :root {
    --canvas: #f3f4f4;
    --paper: #ffffff;
    --frame: #e4e4e4;
    --ink: #1d1d1d;
    --body-ink: #3a3a3a;
    --sky-top: #f9e596;
    --sky-mid: #f6c34a;
    --horizon: #f1a928;
    --sand: #e7952a;
  }
  * { margin: 0; padding: 0; box-sizing: border-box; }
  html, body { width: 1200px; height: 1200px; overflow: hidden; background: var(--canvas); }
  .spread { position: absolute; left: 128px; top: 364px; width: 942px; height: 471px; }
  .cover { position: absolute; left: 0; top: 0; width: 471px; height: 471px; background: var(--paper); }
  .cover-photo { position: absolute; left: 0; top: 0; width: 471px; height: 392px; display: block; }
  .brand { position: absolute; left: 0; width: 100%; display: flex; flex-direction: column; align-items: center; }
  .brand-dot { width: 34px; height: 34px; border-radius: 50%; border: 2px solid var(--ink); }
  .brand-name { font-family: "Mulish", sans-serif; font-weight: 700; color: var(--ink); letter-spacing: 0.3px; white-space: nowrap; }
  .cover .brand { top: 397px; }
  .cover .brand-name { font-size: 12px; margin-top: 4px; }
  .inside { position: absolute; left: 471px; top: 0; width: 471px; height: 471px; background: var(--frame); }
  .inside-page { position: absolute; left: 13px; top: 12px; width: 446px; height: 446px; background: var(--paper); text-align: center; }
  .inside-title { position: absolute; top: 31px; width: 100%; font-family: "Mulish", sans-serif; font-weight: 700; font-size: 13.5px; color: var(--ink); letter-spacing: 0.3px; white-space: nowrap; }
  .copy { position: absolute; top: 83px; width: 100%; font-family: "Questrial", sans-serif; font-size: 7.4px; line-height: 14.5px; color: var(--body-ink); white-space: nowrap; }
  .copy p + p { margin-top: 14px; }
  .divider { position: absolute; top: 228px; width: 100%; font-family: "Questrial", sans-serif; font-size: 11px; letter-spacing: 4px; color: var(--ink); }
  .inside-page .brand { top: 290px; }
  .inside-page .brand-dot { width: 26px; height: 26px; }
  .inside-page .brand-name { font-size: 9px; margin-top: 3px; }
  .contact { position: absolute; top: 353px; width: 100%; font-family: "Open Sans", sans-serif; color: var(--ink); white-space: nowrap; }
  .contact-heading { font-size: 9.2px; font-weight: 700; }
  .contact-note { font-size: 5.4px; line-height: 7.5px; margin-top: 10px; }
  .contact-line { font-size: 7.4px; font-weight: 700; line-height: 11px; }
  .contact-phone { margin-top: 10px; }
</style>
</head>
<body>
  <main class="spread">
    <section class="cover">
      <svg class="cover-photo" viewBox="0 0 471 392" role="img" aria-label="Photo: man standing on a beach at sunset, silhouetted against a golden sky and sea">
        <defs>
          <linearGradient id="sunset" x1="0" y1="0" x2="0" y2="1">
            <stop offset="0" stop-color="#f9e596"/>
            <stop offset="0.45" stop-color="#f6c34a"/>
            <stop offset="0.6" stop-color="#f1a928"/>
            <stop offset="1" stop-color="#e7952a"/>
          </linearGradient>
        </defs>
        <path d="M0 0 H471 V374 C320 376 170 388 0 392 Z" fill="url(#sunset)"/>
      </svg>
      <div class="brand">
        <span class="brand-dot"></span>
        <span class="brand-name">PINECREST</span>
      </div>
    </section>
    <section class="inside">
      <div class="inside-page">
        <h1 class="inside-title">AT PINECREST TREATMENT CENTER</h1>
        <div class="copy">
          <p>We believe strongly in a holistic approach<br>to recovery through treating the mind, body, and soul.</p>
          <p>To facilitate this holistic recovery perspective we promote a healthy diet for our clients,<br>and physical fitness through visits to a nationally recognized gym.</p>
          <p>In addition, guided yoga and meditation, hiking trips<br>in Southern California’s beautiful natural areas,<br>and trips to the world-famous beaches are available during a client’s stay.</p>
        </div>
        <div class="divider">.....</div>
        <div class="brand">
          <span class="brand-dot"></span>
          <span class="brand-name">PINECREST</span>
        </div>
        <div class="contact">
          <p class="contact-heading">Contact Pinecrest Treatment Center Today</p>
          <p class="contact-note">If you require Auxiliary Aid in communicating with our team<br>please reach out to our call center.</p>
          <p class="contact-line contact-phone">855-555-0147</p>
          <p class="contact-line">http://pinecrestcarehub.example</p>
        </div>
      </div>
    </section>
  </main>
</body>
</html>
```